Container Web Design Project

I need the front page of my website to have a new, fresh look.
Our company is a highly specialized marketplace for shipping containers (yes, the 20' and 40' kind). Basically, think of Quibzo for shipping containers.
I have all of the links/content that I need plugged into a wireframe (attached), and the core color (blue #0073a2) of our existing site should stay the same as we've got stationary, business cards, marketing materials...
If you have any questions please ask.

```html
<!DOCTYPE html>
<html lang="en">
<head>
<meta charset="utf-8">
<title>CargoBidHub – Shipping Container Marketplace</title>
<link href="https://fonts.googleapis.com/css2?family=Arimo:wght@400;700&family=Open+Sans:wght@400;600;700&display=swap" rel="stylesheet">
<style>
:root{
  --brand:#0073a2;
  --brand-dark:#005f87;
  --brand-light:#1a8fc4;
  --row:#0a6d99;
  --panel:#e4e4e4;
  --side:#505050;
  --red:#d62a2a;
  --link:#0a77ad;
  --price:#d94030;
  --text:#222;
  --white:#fff;
}
*{box-sizing:border-box;margin:0;padding:0}
html,body{width:810px;height:1200px;overflow:hidden;background:#fff;font-family:Arimo,Arial,sans-serif;color:var(--text)}
.page{position:relative;width:810px;height:1200px}
.abs{position:absolute}

.header{left:0;top:0;width:810px;height:79px;background:linear-gradient(180deg,#1a8fc4,#0073a2)}
.brand-name{left:14px;top:14px;width:207px;height:48px;border:2px solid #fff;border-radius:5px;color:#fff;font-weight:700;font-size:22px;display:flex;align-items:center;justify-content:center;letter-spacing:.3px}
.top-links{right:14px;top:13px;display:flex;gap:22px;color:#fff;font-size:10.5px}
.phone{right:14px;top:36px;display:flex;align-items:center;gap:8px;color:#fff;font-size:25px}
.phone svg{width:30px;height:30px}

.mainnav{left:0;top:79px;width:810px;height:37px;background:var(--brand);border-top:1px solid #3aa6d4;display:flex;justify-content:space-around;align-items:center;color:#fff;font-family:"Open Sans",sans-serif;font-size:11px;padding:0 6px}

.searchbar{left:10px;top:128px;width:790px;height:42px;background:var(--brand);border-radius:9px;padding:6px}
.searchbar .field{position:absolute;left:7px;top:6px;width:465px;height:30px;background:#fff;border-radius:6px;border:1px solid #ccc;font-size:12px;color:#333;display:flex;align-items:center;padding-left:10px;gap:8px}
.select{position:absolute;top:6px;height:30px;background:#fff;border-radius:6px;border:1px solid #ccc;font-size:12px;display:flex;align-items:center;justify-content:space-between;padding:0 6px 0 12px}
.select i{width:18px;height:18px;border-radius:50%;background:#555;display:block;position:relative}
.select i:after{content:"";position:absolute;left:5px;top:6px;border:4px solid transparent;border-top:6px solid #fff}
.search-btn{position:absolute;right:7px;top:5px;width:89px;height:32px;background:var(--red);color:#fff;border-radius:6px;font-weight:700;font-size:17px;display:flex;align-items:center;justify-content:center}

.sidenav{left:10px;top:179px;width:259px;height:292px;background:var(--side);border-radius:6px;padding:5px}
.sidenav a{display:flex;align-items:center;gap:10px;height:31px;margin-bottom:4px;background:linear-gradient(180deg,#1a8fc4,#0073a2);border-radius:4px;color:#fff;font-size:11.5px;text-decoration:none;padding-left:9px}
.bullet{width:14px;height:14px;border-radius:50%;background:var(--red);position:relative;flex:none}
.bullet:after{content:"";position:absolute;left:5px;top:4px;border:3px solid transparent;border-left:5px solid #fff}

.newsletter{left:10px;top:478px;width:259px;height:87px;background:var(--panel);border-radius:6px;padding:14px 13px}
.newsletter h3{font-family:"Open Sans",sans-serif;font-weight:600;font-size:15px;color:#333;margin-bottom:10px}
.nl-row{display:flex;gap:8px}
.nl-input{width:163px;height:30px;background:#888;border-radius:6px;color:#eee;font-size:12.5px;display:flex;align-items:center;padding-left:10px}
.nl-btn{width:64px;height:30px;background:var(--red);border-radius:6px;color:#fff;font-size:10px;font-weight:700;display:flex;align-items:center;justify-content:center}

.partner{left:10px;width:255px;display:flex;align-items:center;gap:10px;font-weight:700;color:#1d2c6b;font-size:26px}
.partner .sq{width:22px;height:22px;background:#1d2c6b;flex:none}
.partner.boxed{background:#f2f2f2;height:92px;padding-left:20px}

.mainpanel{left:279px;top:179px;width:521px;height:461px;background:var(--panel);border-radius:6px}
.map{left:285px;top:186px;width:508px;height:271px;background:var(--brand);border-radius:6px;padding:6px}
.map div{width:100%;height:100%;background:linear-gradient(135deg,#a9c6e6 0%,#c8d9b8 45%,#e8e2cc 60%,#a9c6e6 100%);border-radius:3px}
.carousel{left:285px;top:471px;width:508px;height:160px}
.arrow{position:absolute;top:34px;width:0;height:0;border-top:24px solid transparent;border-bottom:24px solid transparent}
.arrow.l{left:0;border-right:14px solid #aaa}
.arrow.r{right:0;border-left:14px solid #aaa}
.cards{position:absolute;left:25px;top:0;display:flex;gap:6px}
.card{width:86px}
.card .box{background:#d6d6d6;border-radius:3px;height:116px;padding:4px}
.card .photo{height:57px}
.card .t{color:var(--link);font-weight:700;font-size:9.5px;line-height:10px;margin-top:5px}
.card .s{color:#444;font-size:8.5px;line-height:9px;margin-top:4px}
.card .loc{font-size:10px;line-height:11px;color:#444;margin-top:7px;padding-left:3px}
.card .pr{color:var(--price);font-size:10px;margin-top:3px;padding-left:3px}

.listpanel{left:279px;top:655px;width:521px;height:376px;background:var(--panel);border-radius:6px;padding:7px}
.listing{display:flex;height:68px;margin-bottom:5px;background:var(--row);border-radius:6px;padding:6px 7px;color:#fff}
.listing .photo{width:81px;height:56px;flex:none}
.listing .mid{width:245px;padding-left:11px}
.listing h4{font-size:11.5px;font-weight:700;margin-bottom:5px}
.listing p{font-size:9.5px;line-height:10px}
.listing .meta{padding-left:25px;font-size:10px;line-height:12.5px;padding-top:1px}

.copyright{left:17px;top:1074px;width:780px;font-size:9.5px;line-height:12px;color:#222}
.footer{left:0;top:1120px;width:810px;height:80px;background:var(--brand);color:#fff;font-size:10px;line-height:12px}
.footer ul{position:absolute;top:17px;list-style:none}
</style>
</head>
<body>
<div class="page">
  <header class="header abs">
    <div class="brand-name abs">cargobidhub</div>
    <nav class="top-links abs"><span>Create Account</span><span>Login</span><span>About CargoBidHub.com</span></nav>
    <div class="phone abs">
      <svg viewBox="0 0 30 30"><circle cx="15" cy="15" r="13" fill="none" stroke="#fff" stroke-width="2"/><path d="M10 8c1-1 2-1 3 1l1 3-2 2c1 2 3 4 5 5l2-2 3 1c2 1 2 2 1 3-2 2-5 2-9-2s-6-8-4-11z" fill="#fff"/></svg>
      (555) 014-2270
    </div>
  </header>
  <nav class="mainnav abs"><span>20' Shipping Containers</span><span>40' Shipping Containers</span><span>40' High Cube Container</span><span>Open Top Containers</span><span>How to Buy a Shipping Container</span></nav>

  <div class="searchbar abs">
    <div class="field"><svg width="14" height="14" viewBox="0 0 14 14"><circle cx="5.5" cy="5.5" r="4" fill="none" stroke="#444" stroke-width="2"/><path d="M8.5 8.5l4 4" stroke="#444" stroke-width="2.4"/></svg>City, State or Country</div>
    <div class="select" style="left:490px;width:122px">Container Type<i></i></div>
    <div class="select" style="left:618px;width:66px">Units<i></i></div>
    <div class="search-btn">search</div>
  </div>

  <nav class="sidenav abs">
    <a><span class="bullet"></span>How to Buy Shipping Containers</a>
    <a><span class="bullet"></span>New Listings</a>
    <a><span class="bullet"></span>News and Articles</a>
    <a><span class="bullet"></span>About CargoBidHub.com</a>
    <a><span class="bullet"></span>Container Weights and Dimensions</a>
    <a><span class="bullet"></span>CargoBidHub.com FAQs</a>
    <a><span class="bullet"></span>Shipping Container Terms</a>
    <a><span class="bullet"></span>How to Sell Your Containers</a>
  </nav>

  <section class="newsletter abs">
    <h3>Subscribe to Our Newsletter</h3>
    <div class="nl-row"><div class="nl-input">enter email</div><div class="nl-btn">subscribe</div></div>
  </section>

  <div class="partner abs" style="top:612px">Boxwell</div>
  <div class="partner boxed abs" style="top:697px">Ironhold Units <span class="sq"></span></div>
  <div class="partner abs" style="top:845px">Nordsea Freight</div>
  <div class="partner abs" style="top:955px">Keelmark</div>

  <div class="mainpanel abs"></div>
  <div class="map abs"><div role="img" aria-label="Map of North America with red pins marking container listing locations"></div></div>

  <div class="carousel abs">
    <span class="arrow l"></span><span class="arrow r"></span>
    <div class="cards">
      <div class="card"><div class="box"><div class="photo" role="img" aria-label="Stacked red shipping containers" style="background:linear-gradient(#c9d8e8,#c0574a)"></div><div class="t">#2712 - 45' high cube containers</div><div class="s">40' High cube container</div></div><div class="loc">Chicago, IL<br>United States</div><div class="pr">USD 5300</div></div>
      <div class="card"><div class="box"><div class="photo" role="img" aria-label="Container doors, olive grey" style="background:linear-gradient(#9b9a86,#6f6f5e)"></div><div class="t">#2712 - 45' high cube containers</div><div class="s">40' High cube container</div></div><div class="loc">Chicago, IL<br>United States</div><div class="pr">USD 5300</div></div>
      <div class="card"><div class="box"><div class="photo" role="img" aria-label="Blue shipping container" style="background:linear-gradient(#4f86c8,#1f5fa8)"></div><div class="t">#2712 - 45' high cube containers</div><div class="s">40' High cube container</div></div><div class="loc">Chicago, IL<br>United States</div><div class="pr">USD 5300</div></div>
      <div class="card"><div class="box"><div class="photo" role="img" aria-label="Inside of an empty white container" style="background:linear-gradient(#f2f2f2,#bdbdbd)"></div><div class="t">#2712 - 45' high cube containers</div><div class="s">40' High cube container</div></div><div class="loc">Chicago, IL<br>United States</div><div class="pr">USD 5300</div></div>
      <div class="card"><div class="box"><div class="photo" role="img" aria-label="Orange shipping container" style="background:linear-gradient(#e39a4c,#c46a1f)"></div><div class="t">#2712 - 45' high cube containers</div><div class="s">40' High cube container</div></div><div class="loc">Chicago, IL<br>United States</div><div class="pr">USD 5300</div></div>
    </div>
  </div>

  <section class="listpanel abs">
    <article class="listing"><div class="photo" role="img" aria-label="Container doors photo" style="background:linear-gradient(#a3a28c,#6f6f5e)"></div><div class="mid"><h4>#2712 - 45' high cube containers</h4><p>40' shipping container with doors at each end for sale in Long Beach, CA. This container is a New One Trip condition unit and available for immediate pick up.</p></div><div class="meta">40' High cube container<br>Chicago, IL United States<br>price: USD 5300</div></article>
    <article class="listing"><div class="photo" role="img" aria-label="Container doors photo" style="background:linear-gradient(#a3a28c,#6f6f5e)"></div><div class="mid"><h4>#2712 - 45' high cube containers</h4><p>40' shipping container with doors at each end for sale in Long Beach, CA. This container is a New One Trip condition unit and available for immediate pick up.</p></div><div class="meta">40' High cube container<br>Chicago, IL United States<br>price: USD 5300</div></article>
    <article class="listing"><div class="photo" role="img" aria-label="Container doors photo" style="background:linear-gradient(#a3a28c,#6f6f5e)"></div><div class="mid"><h4>#2712 - 45' high cube containers</h4><p>40' shipping container with doors at each end for sale in Long Beach, CA. This container is a New One Trip condition unit and available for immediate pick up.</p></div><div class="meta">40' High cube container<br>Chicago, IL United States<br>price: USD 5300</div></article>
    <article class="listing"><div class="photo" role="img" aria-label="Container doors photo" style="background:linear-gradient(#a3a28c,#6f6f5e)"></div><div class="mid"><h4>#2712 - 45' high cube containers</h4><p>40' shipping container with doors at each end for sale in Long Beach, CA. This container is a New One Trip condition unit and available for immediate pick up.</p></div><div class="meta">40' High cube container<br>Chicago, IL United States<br>price: USD 5300</div></article>
    <article class="listing"><div class="photo" role="img" aria-label="Container doors photo" style="background:linear-gradient(#a3a28c,#6f6f5e)"></div><div class="mid"><h4>#2712 - 45' high cube containers</h4><p>40' shipping container with doors at each end for sale in Long Beach, CA. This container is a New One Trip condition unit and available for immediate pick up.</p></div><div class="meta">40' High cube container<br>Chicago, IL United States<br>price: USD 5300</div></article>
  </section>

  <p class="copyright abs">Copyright © 2011-2013 CargoBidHub, Inc. All Rights Reserved. CargoBidHub.com is a trademark of CargoBidHub Inc. Designated trademarks and brands are the property of their respective owners. Use of this Web site constitutes acceptance of the CargoBidHub user agreement and privacy policy.</p>

  <footer class="footer abs">
    <ul style="left:20px"><li>Privacy Policy</li><li>User Agreement</li><li>Help</li></ul>
    <ul style="left:198px"><li>About CargoBidHub.com</li><li>News and Articles</li><li>Contact Information</li></ul>
    <ul style="left:421px"><li>Container Dimensions and &nbsp;Weights</li><li>Glossary</li></ul>
    <ul style="left:693px"><li>Browse Locations</li></ul>
  </footer>
</div>
</body>
</html>
```